Box design for superfood powders

Hey,
I am creating a new brand of superfoods mixes in and I am looking for a designer to create the design for the box.
I have for 4 products on the roadmap, but I need the design just for the first one:
- For skin nails and hair benefits: Collagen + CoQ10 and Vitamin C powders (eg: Blueberries, Camu Camu, Acai)
- For energy and immune system (eg: mushrooms powder)
- Green Mix (eg: Spirulina + Wheatgrass + Chlorella)
- Protein mix (eg: hemp + rice powders)
I will use Kraft paper for the box so I am able to print max 2 colors on them (black and another color distinctive for each specific powder mix).
I need the design just for the first one with collagen, because all the products will have the same format. I will just change the name, ingredients and the color
More details in the archive attached.

Updates
Low design quality
Target Market(s)
woman between 30-50
Requirements
Should not have
- Ilustrations with fruits or flowers
Just shapes and colors

```html
<!DOCTYPE html>
<html lang="en">
<head>
<meta charset="utf-8">
<title>Radiant Collagen – sachet dieline</title>
<link rel="stylesheet" href="https://fonts.googleapis.com/css2?family=Poppins:wght@500&family=Encode+Sans+Semi+Condensed:wght@400;600;700&display=swap">
<style>
  :root {
    --page: #ffffff;
    --kraft: #c99a6c;
    --kraft-light: #d3a67a;
    --kraft-dark: #bf8f60;
    --ink: #161311;
    --cut: #1b1b1b;
    --bleed: #b8362f;
    --fold: #e0a48c;
  }
  * { box-sizing: border-box; margin: 0; padding: 0; }
  html, body { width: 1200px; height: 1200px; overflow: hidden; background: var(--page); }
  body { position: relative; font-family: "Encode Sans Semi Condensed", "Arial Narrow", sans-serif; color: var(--ink); }

  .sheet {
    position: absolute; left: 372px; top: 75px; width: 455px; height: 1050px;
    background: radial-gradient(ellipse at 30% 20%, var(--kraft-light), var(--kraft) 55%, var(--kraft-dark));
  }
  .cut-line { position: absolute; left: 27px; top: 25px; width: 401px; height: 1000px; border: 1.5px solid var(--cut); }
  .bleed-v { position: absolute; top: 25px; height: 1000px; width: 0; border-left: 1.2px solid var(--bleed); }
  .bleed-v.left { left: 52px; }
  .bleed-v.right { left: 402px; }
  .bleed-h { position: absolute; left: 27px; width: 401px; height: 0; border-top: 1.2px solid var(--bleed); }
  .bleed-h.top { top: 50px; }
  .bleed-h.bottom { top: 1000px; }
  .fold-line { position: absolute; left: 27px; top: 525px; width: 401px; border-top: 1.2px solid var(--fold); }

  .panel { position: absolute; left: 52px; width: 350px; height: 475px; }
  .panel-front { top: 50px; }
  .panel-back { top: 525px; transform: rotate(180deg); }

  /* front */
  .brand {
    position: absolute; left: 0; top: 62px; width: 100%; text-align: center;
    font-family: "Encode Sans Semi Condensed", sans-serif; font-weight: 700; font-size: 22px; letter-spacing: 0.5px;
  }
  .product-name {
    position: absolute; left: 0; top: 140px; width: 100%; text-align: center;
    font-family: "Poppins", sans-serif; font-weight: 500; font-size: 35px; line-height: 44px;
  }
  .intro {
    position: absolute; left: 30px; top: 240px; width: 292px;
    font-size: 11.2px; line-height: 13.6px; font-weight: 600; text-align: justify;
  }
  .rule { position: absolute; left: 30px; top: 336px; width: 292px; border-top: 1px solid var(--ink); }
  .badge { position: absolute; left: 36px; top: 356px; width: 38px; height: 38px; border: 1.6px solid var(--ink); border-radius: 50%; }
  .ingredients { position: absolute; left: 88px; top: 352px; width: 240px; font-size: 9.4px; line-height: 12px; font-weight: 600; }
  .ingredients h3 { font-size: 10px; font-weight: 700; }

  /* back */
  .free-from { position: absolute; left: 22px; top: 26px; width: 230px; font-size: 9px; line-height: 11px; font-weight: 600; }
  .free-from b { font-weight: 700; display: block; }
  .free-icons { position: absolute; right: 22px; top: 28px; display: flex; gap: 8px; }
  .free-icons svg { width: 30px; height: 30px; }
  .usage-art { position: absolute; left: 40px; top: 105px; width: 68px; height: 50px; background: linear-gradient(var(--kraft-light), var(--kraft-dark)); border-radius: 4px; }
  .nutrition { position: absolute; right: 22px; top: 118px; width: 140px; border: 1px solid var(--ink); font-size: 9px; font-weight: 600; }
  .nutrition header { text-align: center; border-bottom: 1px solid var(--ink); padding: 3px 0 4px; line-height: 11px; font-weight: 400; }
  .nutrition header b { display: block; font-size: 11px; font-weight: 700; }
  .nutrition ul { list-style: none; padding: 5px 7px; line-height: 14.5px; }
  .nutrition li { display: flex; justify-content: space-between; }
  .info { position: absolute; left: 22px; width: 160px; font-size: 8.8px; line-height: 11px; font-weight: 600; }
  .info b { font-weight: 700; display: block; }
  .how { top: 165px; }
  .storage { top: 228px; left: 34px; }
  .produced { top: 290px; }
  .connect { top: 330px; }
  .dates { position: absolute; left: 22px; top: 412px; font-size: 8.8px; line-height: 18px; font-weight: 600; }
  .weight { position: absolute; right: 22px; top: 432px; font-size: 10px; font-weight: 700; }
</style>
</head>
<body>
  <div class="sheet">
    <div class="cut-line"></div>
    <div class="bleed-v left"></div>
    <div class="bleed-v right"></div>
    <div class="bleed-h top"></div>
    <div class="bleed-h bottom"></div>
    <div class="fold-line"></div>

    <section class="panel panel-front">
      <div class="brand">Velora</div>
      <h1 class="product-name">Radiant<br>Collagen</h1>
      <p class="intro">We make it easy for busy people to look and feel good about their appearance. Just add Radiant Collagen powder to your favorite smoothie or milk and get the extra dose of collagen and skin protecting antioxidants. It helps combat the effects of free radicals and may restore your natural plumpness.</p>
      <div class="rule"></div>
      <div class="badge"></div>
      <div class="ingredients">
        <h3>Ingredients:</h3>
        <p>• Type 1 Marine Collagen • CoQ10<br>• Hyaluronic acid powder • Camu Camu • Rosehip<br>• Sea buckthorn • Banana • Date • Acai</p>
      </div>
    </section>

    <section class="panel panel-back">
      <p class="free-from"><b>Free from:</b>Gluten, Dairy, Soy, GMO, sweeteners, fillers, additives, preservatives or anything artificial.</p>
      <div class="free-icons">
        <svg viewBox="0 0 30 30"><circle cx="15" cy="15" r="13" fill="none" stroke="#161311" stroke-width="2"/><line x1="6" y1="6" x2="24" y2="24" stroke="#161311" stroke-width="2"/></svg>
        <svg viewBox="0 0 30 30"><circle cx="15" cy="15" r="13" fill="none" stroke="#161311" stroke-width="2"/><line x1="6" y1="6" x2="24" y2="24" stroke="#161311" stroke-width="2"/></svg>
      </div>
      <div class="usage-art" role="img" aria-label="Line drawing of a sachet being poured into a cup"></div>
      <div class="nutrition">
        <header><b>Nutrition Value table</b>Per sachet</header>
        <ul>
          <li><span>Lorem Ipsum</span><span>: 00 KKal</span></li>
          <li><span>Lorem Ipsum</span><span>: 00 KKal</span></li>
          <li><span>Lorem Ipsum</span><span>: 00 KKal</span></li>
          <li><span>Lorem Ipsum</span><span>: 00 KKal</span></li>
          <li><span>Lorem Ipsum</span><span>: 00 KKal</span></li>
          <li><span>Lorem Ipsum</span><span>: 00 KKal</span></li>
          <li><span>Lorem Ipsum</span><span>: 00 KKal</span></li>
        </ul>
      </div>
      <p class="info how"><b>How to use it:</b>Add one pack to your water, smoothies, yoghurt, musli, oatmeal.</p>
      <p class="info storage"><b>Storage:</b>Keep closed in a cool dry place</p>
      <p class="info produced"><b>Produced by:</b>Norva SRL for Brightleaf SRL</p>
      <p class="info connect"><b>Connect:</b>Call +40 000 0000 000<br>website:<br><b>www.velora-example.com/start</b></p>
      <p class="dates">MANUFACTURED DATE :<br>BEST BEFORE :</p>
      <p class="weight">Net. Wght. 10 g</p>
    </section>
  </div>
</body>
</html>
```